Medical Practice Business Card

we need a business card for our new medical ophthalmology practice based in Needham Massachusetts. we are looking for a simple , modern and elegant design.
the card needs to contain the following
1- the logo of our practice (please see attached file)
2- the name of the practice : "Silver Birch Retina Care"
3- Doctor's Name: Tobias Rendell MD PhD
4- Specialty: Board-Certified Vitreoretinal Surgeon
5- practice address: 87 Larkspur Ave, Suite 210, Needham MA 02481
7- Office number: 617- 482 - 7730
8- fax number: 617- 391 - 2268
9- email: info@sbretinahub.example
10- website: www.sbretinahub.example

```html
<!DOCTYPE html>
<html lang="en">
<head>
<meta charset="utf-8">
<title>Silver Birch Retina Care – Business Card</title>
<link href="https://fonts.googleapis.com/css2?family=Arimo:wght@400;700&display=swap" rel="stylesheet">
<style>
  :root {
    --backdrop: #3c3c3c;
    --card: #173f6d;
    --card-edge: #6fd6ea;
    --name-blue: #3b92d8;
    --text-light: #f2f5fa;
    --rule: #4aa6e0;
  }
  * { box-sizing: border-box; margin: 0; padding: 0; }
  html, body {
    width: 1200px; height: 803px; overflow: hidden;
    background: var(--backdrop);
  }
  .sheet {
    width: 1200px; height: 803px;
    display: flex; align-items: center; justify-content: center; gap: 44px;
  }
  .card {
    width: 540px; height: 308px;
    background: var(--card);
    border-radius: 22px;
    border-bottom: 3px solid var(--card-edge);
    box-shadow: 0 18px 36px rgba(0,0,0,.45);
    display: flex; flex-direction: column; align-items: center; justify-content: center;
    color: var(--text-light);
    font-family: "Arimo", Arial, sans-serif;
  }
  .doctor-name {
    font-weight: 700; font-size: 25px; letter-spacing: .5px;
    color: var(--name-blue);
  }
  .specialty { font-size: 13px; margin-top: 4px; }
  .divider { margin: 14px 0 22px; }
  .address { font-size: 13.5px; }
  .contact-row {
    display: flex; align-items: center; gap: 6px;
    font-size: 13.5px; margin-top: 6px;
  }
  .contact-row svg { width: 12px; height: 12px; fill: var(--name-blue); }
  .contact-row .sep { width: 8px; }
  .website { font-size: 13.5px; margin-top: 6px; }

  .brand-name {
    font-family: "Arimo", Arial, sans-serif; font-weight: 400;
    font-size: 30px; line-height: 1.2; color: var(--text-light);
    text-align: center;
  }
</style>
</head>
<body>
<main class="sheet">
  <section class="card card-info">
    <h1 class="doctor-name">TOBIAS RENDELL MD PHD</h1>
    <p class="specialty">Board-Certified Vitreoretinal Surgeon</p>
    <svg class="divider" width="150" height="8" viewBox="0 0 150 8" aria-hidden="true">
      <circle cx="4" cy="4" r="3" fill="var(--rule)"/>
      <line x1="4" y1="4" x2="150" y2="4" stroke="var(--rule)" stroke-width="1.2"/>
    </svg>
    <p class="address">87 Larkspur Ave, Suite 210, Needham MA 02481</p>
    <p class="contact-row">
      <svg viewBox="0 0 24 24" aria-label="Phone"><path d="M6.6 10.8a15.1 15.1 0 0 0 6.6 6.6l2.2-2.2c.3-.3.7-.4 1-.2 1.1.4 2.3.6 3.6.6.6 0 1 .4 1 1V20c0 .6-.4 1-1 1A17 17 0 0 1 3 4c0-.6.4-1 1-1h3.5c.6 0 1 .4 1 1 0 1.3.2 2.5.6 3.6.1.3 0 .7-.2 1z"/></svg>
      <span>617- 482 - 7730</span><span class="sep"></span>
      <svg viewBox="0 0 24 24" aria-label="Fax"><path d="M6 2h10v5H6zM3 8h18v10h-3v4H6v-4H3zm5 7v5h8v-5z"/></svg>
      <span>617- 391 - 2268</span><span class="sep"></span>
      <svg viewBox="0 0 24 24" aria-label="Email"><path d="M2 5h20v14H2zm2 2v.5l8 5 8-5V7z"/></svg>
      <span>info@sbretinahub.example</span>
    </p>
    <p class="website">www.sbretinahub.example</p>
  </section>

  <section class="card card-brand">
    <p class="brand-name">Silver Birch Retina Care</p>
  </section>
</main>
</body>
</html>
```